Header image for law blog

I need a header image for my blog at www.prairiecourtledger.net.

The colors would match the current site. It would say: "Court Ledger: Estate Planning and Real Estate in the Land of Lincoln."

I also want to add in smaller type "Law Office of Ned Pyrkett 555 014 7283 ned@kettbar.com."

The theme maker suggests a header size of 1600 × 230 pixels.

```html
<!DOCTYPE html>
<html lang="en">
<head>
<meta charset="utf-8">
<title>Court Ledger – Blog Header</title>
<link href="https://fonts.googleapis.com/css2?family=Ruluko&display=swap" rel="stylesheet">
<style>
  :root {
    --paper: #f5f1e2;
    --ink: #111111;
  }
  html, body {
    margin: 0;
    padding: 0;
    width: 1200px;
    height: 230px;
    overflow: hidden;
    background: var(--paper);
  }
  .blog-header {
    position: relative;
    width: 1200px;
    height: 230px;
    background: var(--paper);
    color: var(--ink);
    font-family: "Ruluko", sans-serif;
  }
  .blog-title,
  .blog-tagline,
  .office-contact {
    position: absolute;
    margin: 0;
    font-weight: 400;
    white-space: nowrap;
    line-height: 1;
  }
  .blog-title {
    left: 123px;
    top: 20px;
    font-size: 56px;
    letter-spacing: -1px;
  }
  .blog-tagline {
    left: 92px;
    top: 104px;
    font-size: 38px;
    letter-spacing: -0.6px;
  }
  .office-contact {
    right: 4px;
    top: 198px;
    font-size: 20px;
    letter-spacing: -0.4px;
  }
</style>
</head>
<body>
  <header class="blog-header">
    <h1 class="blog-title">Court Ledger</h1>
    <p class="blog-tagline">Estate Planning and Real Estate in the Land of Lincoln.</p>
    <p class="office-contact">I also want to add in smaller type "Law Office of Ned Pyrkett 555 014 7283 ned@kettbar.com.</p>
  </header>
</body>
</html>
```